Flyer-Design für 3D Art aus Blech/Metall
Zielgruppe
3D Art aus Blech/Metall
Individuelles Design auf Kundenwunsch
Aufgabenstellung
Informationen anhand Vorlage im Anhang.
Flyer im Format A5 hoch oder quer
Hochwertiges & modernes Erscheinungsbild
Bilder von der Webseite nehmen www.vetrani.ch

```html
<!DOCTYPE html>
<html lang="de">
<head>
<meta charset="utf-8">
<title>Design &amp; Art by vetrani.ch – Flyer</title>
<link href="https://fonts.googleapis.com/css2?family=Inter:wght@300;400;500&display=swap" rel="stylesheet">
<style>
  :root {
    --paper: #e9e8e3;
    --ink: #111111;
    --ink-soft: #3a3a38;
    --rule: #4a4a48;
    --rust: #b8643a;
    --rust-dark: #8e4526;
    --leaf: #7ea346;
    --stone: #b9bcb8;
  }
  * { margin: 0; padding: 0; box-sizing: border-box; }
  html, body {
    width: 1200px;
    height: 864px;
    overflow: hidden;
    background: var(--paper);
  }
  .flyer {
    position: relative;
    width: 1200px;
    height: 864px;
    background: var(--paper);
    font-family: "Inter", "Helvetica Neue", Arial, sans-serif;
    color: var(--ink);
  }
  .tagline {
    position: absolute;
    left: 585px;
    top: 38px;
    font-size: 15px;
    font-weight: 500;
    letter-spacing: 0.02em;
    text-transform: uppercase;
    color: var(--ink);
  }
  .headline {
    position: absolute;
    right: 668px;
    top: 172px;
    text-align: right;
    font-size: 70px;
    font-weight: 400;
    line-height: 84px;
    letter-spacing: -0.01em;
  }
  .divider {
    position: absolute;
    left: 563px;
    top: 185px;
    width: 1px;
    height: 192px;
    background: var(--rule);
  }
  .contact {
    position: absolute;
    left: 585px;
    top: 398px;
    font-size: 15px;
    font-weight: 300;
    line-height: 26px;
    color: var(--ink-soft);
  }
  .work-photo {
    position: absolute;
    left: 585px;
    top: 468px;
    width: 520px;
    height: 300px;
    background: linear-gradient(180deg,
      var(--leaf) 0%,
      var(--rust) 30%,
      var(--rust-dark) 70%,
      var(--stone) 100%);
  }
</style>
</head>
<body>
  <main class="flyer">
    <p class="tagline">Blechdesign aus Seewilen</p>

    <h1 class="headline">Design &amp; Art<br>by vetrani.ch</h1>

    <div class="divider"></div>

    <address class="contact">
      Lukas Brändli | 079 318 62 07<br>
      lbraendli@mailpost.ch | vetrani.ch
    </address>

    <div class="work-photo" role="img" aria-label="Foto: rostrotes Metallpaneel mit ausgeschnittenem Drachenmotiv im Garten vor Bambus und Steinlaterne"></div>
  </main>
</body>
</html>
```